Web Design Project

I need designs (PSD only - no programming) for several pages of a new website helping train operators to manage key information about their traindrivers.
The main feature of this website is the management of personnel records (create, edit, search, delete). Another key aspect is the management of user privileges. Since this is a new website we also need a user friendly frontpage, pricing information and how it works sections.
This can be broken down into 9 pages for which we need designs (PSDs).
1. Home
2. Driver record
3. How it works
4. Pricing
5. User administration
6. Help
7. Record list view
8. Login
9. Registration
Navigation (not logged in) are: Home | How it works | Pricing | Customers | About us | Contact
Navigation (logged in) are: Overview | Administration | Manage records | Billing | Help | Contact
Footer: Customer logos | Awards | Terms & Conditions | Privacy
To provide the best support for you to come up with a strong design proposal I will provide DAILY feedback to all participants. We have also created concept mockups (attached) and example pages (below) for each section to give you a clear sense of what we look for.
The core concepts for a successful bid are that the website is EASY to understand, INTUITIVE to navigate, and SIMPLE to use. Most of our users lack technical background and are looking for tool to simplify their work.
The strongest participants (winner and close contenders) will have the opportunity to additional commissioned work on additional sections not included in this brief.
Example Pages (by section)
1. http://www.quorvane.example/site-keepers/
1. http://www.vrm.example/
1. http://www.tovasko.example/
1. http://www.glimmerhootz.example/
2. http://www.pendlo.example/profile_edit.gne
3. https://www.drav.example/how-it-works/
3. http://www.wexalot.example/learn
4. http://www.brindlequay.example/crm/editions-pricing.jsp
4. http://www.quorvane.example/site-keepers/rates
6. https://support.zoltu.example/en-gb/
6. http://help.harbenquill.example/contact_us
8. https://www.morvelnet.example/uas/login
8. https://www.harbenquill.example/login
8. http://www.ublix.example/login/index
For form designs we like Ferrowen, Okvo, Pendlo, Morvelnet, Trellimap and the concepts presented by Dario Fenstermack in his classic Panel Craft Beyond the Checkboxes.
For additional guidance see mockups attached!
Target Market(s)
Security, human resources and admin support employees for train operators.
Industry/Entity Type
Learn
Requirements
Should not have
- Home page should not have
Social media icons (trellimap, pellomb, Morvelnet, RSS feed)
Contact forms
Read more links
Old trains

```html
<!DOCTYPE html>
<html lang="en">
<head>
<meta charset="utf-8">
<title>Drivlane – Prices</title>
<link href="https://fonts.googleapis.com/css2?family=Montserrat:wght@300;400;500;700&display=swap" rel="stylesheet">
<style>
:root{
  --navy:#1c4466;
  --orange:#f7931e;
  --orange-dark:#ef5f22;
  --sky:#5fc0e2;
  --text:#555;
  --muted:#8a8a8a;
  --rule:#dedede;
  --mark:#aaa09d;
}
*{margin:0;padding:0;box-sizing:border-box}
html,body{width:1000px;height:1200px;overflow:hidden;background:#fff;font-family:'Montserrat',sans-serif;color:var(--text)}
.site-header{position:absolute;left:0;top:0;width:1000px;height:96px;background:linear-gradient(#fff 0,#fff 30px,#dcdcdc 88px);border-bottom:8px solid var(--orange)}
.utility{position:absolute;top:12px;left:748px;display:flex;gap:15px;font-size:9.5px;color:#444}
.brand{position:absolute;left:103px;top:36px;font-size:29px;font-weight:700;color:#4ab3d3;letter-spacing:-0.5px}
.main-nav{position:absolute;top:42px;left:0;width:1000px;height:30px}
.main-nav a{position:absolute;top:0;line-height:28px;font-size:14px;font-weight:500;color:var(--navy);text-decoration:none}
.main-nav a.active{background:linear-gradient(#8ed8ef,#4fb6dd);color:#fff;border-radius:5px;padding:0 11px;width:63px}
.main-nav a.active::after{content:"";position:absolute;left:25px;top:28px;border:6px solid transparent;border-top-color:#4fb6dd}
.section-title{position:absolute;left:102px;top:120px;font-size:17px;font-weight:700;color:var(--navy)}
.rule{position:absolute;left:102px;width:796px;height:2px;background:var(--rule)}
.plan{position:absolute;top:177px;height:326px;background:linear-gradient(#f1f0f5,#d6d5df);text-align:center}
.plan-head{height:66px;background:linear-gradient(#b0a6a4,#978d8a);color:#fff;padding-top:13px}
.plan-head .tag{display:block;font-size:14px;font-weight:300}
.plan-head .name{display:block;font-size:19px;font-weight:700;letter-spacing:.5px;margin-top:0}
.plan-body{padding-top:18px;font-size:12px;line-height:20px;font-weight:500;color:var(--text)}
.plan-body .price,.plan-body .strong{color:#111}
.plan-body .gap{height:20px}
.trial{position:absolute;left:50%;transform:translateX(-50%);top:272px;width:153px;height:33px;border-radius:4px;background:linear-gradient(#d4d4d4,#9c9c9c);border:1px solid #8f8f8f;color:#fff;font-size:12px;font-weight:700;line-height:31px}
.plan.featured{top:166px;height:340px;background:linear-gradient(#fff3ec,#fcc9ae);border:3px solid #fff;box-shadow:0 4px 10px rgba(0,0,0,.3)}
.plan.featured .plan-head{background:linear-gradient(#f47c3c,var(--orange-dark));padding-top:11px}
.plan.featured .trial{top:276px;height:41px;line-height:39px;background:linear-gradient(#fba34c,#f06a1f);border-color:#e76a20}
.intro{position:absolute;left:120px;top:568px;width:760px;text-align:center;font-size:13.5px;line-height:19px;color:#777}
.partners-title{position:absolute;left:102px;top:680px;font-size:16px;font-weight:700;color:#999}
.top-bump{position:absolute;left:472px;top:686px}
.partner-row{position:absolute;left:102px;top:726px}
.site-footer{position:absolute;left:102px;top:803px;width:796px;font-size:10px;color:var(--muted);display:flex;justify-content:space-between}
.site-footer a{color:#4a5d98;text-decoration:none}
</style>
</head>
<body>
<header class="site-header">
  <nav class="utility"><span>Sign Up</span><span>Login</span><span>Language</span></nav>
  <div class="brand">Drivlane</div>
  <nav class="main-nav">
    <a style="left:358px" href="#">Home</a>
    <a style="left:427px" href="#">How it Works</a>
    <a class="active" style="left:533px" href="#">Prices</a>
    <a style="left:614px" href="#">Our Customers</a>
    <a style="left:741px" href="#">About Us</a>
    <a style="left:831px" href="#">Contact</a>
  </nav>
</header>

<h1 class="section-title">Price</h1>
<div class="rule" style="top:145px"></div>

<div class="plan" style="left:104px;width:198px">
  <div class="plan-head"><span class="tag">Ultimate</span><span class="name">PLATINUM</span></div>
  <div class="plan-body"><div class="price">200 EUR / month</div><div>(or just 1999 EUR/year)</div><div class="gap"></div><div>20,000 stored pages</div><div>20,000 page modifications</div><div>200,000 pageviews /</div><div class="strong">Auto change notification</div></div>
  <div class="trial">15-DAY FREE TRIAL</div>
</div>
<div class="plan" style="left:305px;width:194px">
  <div class="plan-head"><span class="tag">More Pageviews</span><span class="name">GOLD</span></div>
  <div class="plan-body"><div class="price">50 EUR / month</div><div>(or just 499 EUR/year)</div><div>5,000 stored pages</div><div>5,000 page modifications</div><div>50,000 pageviews /month</div><div class="gap"></div><div>Auto change notification</div><div>1-click XLIFF upload</div></div>
  <div class="trial">15-DAY FREE TRIAL</div>
</div>
<div class="plan" style="left:704px;width:194px">
  <div class="plan-head" style="padding-top:13px"><span class="tag">Basic Plan</span><span class="name">BRONZE</span></div>
  <div class="plan-body" style="padding-top:12px"><div class="price">50 EUR / month</div><div>(or just 499 EUR/year)</div><div>5,000 stored pages</div><div>5,000 page modifications</div><div>50,000 pageviews /month</div><div class="gap"></div><div>Auto change notification</div><div>1-click XLIFF upload</div></div>
  <div class="trial">15-DAY FREE TRIAL</div>
</div>
<div class="plan featured" style="left:499px;width:206px">
  <div class="plan-head"><span class="tag">Most Popular</span><span class="name">SILVER</span></div>
  <div class="plan-body" style="padding-top:24px"><div class="price">200 EUR / month</div><div>(or just 1999 EUR/year)</div><div class="gap"></div><div>20,000 stored pages</div><div>20,000 page modifications</div><div>200,000 pageviews /</div><div class="strong">Auto change notification</div></div>
  <div class="trial">15-DAY FREE TRIAL</div>
</div>

<p class="intro">Lorem Ipsum is simply dummy text of the printing and typesetting industry. Lorem Ipsum has been the industry's standard dummy text ever since the 1500s, when an unknown printer took a galley of type and scrambled it to make a type specimen book. It has survived not only five centuries.</p>

<h2 class="partners-title">Our Partners:</h2>
<svg class="top-bump" width="82" height="24" viewBox="0 0 82 24" aria-label="Back to top">
  <defs><linearGradient id="bump" x1="0" y1="0" x2="0" y2="1"><stop offset="0" stop-color="#f2f2f2"/><stop offset="1" stop-color="#e0e0e0"/></linearGradient></defs>
  <path d="M0 24 A41 30 0 0 1 82 24 Z" fill="url(#bump)"/>
  <path d="M35 13 L41 8 L47 13" fill="none" stroke="#999" stroke-width="2.5"/>
</svg>
<div class="rule" style="top:708px"></div>

<svg class="partner-row" width="796" height="50" viewBox="0 0 796 50" role="img" aria-label="Partner badges">
  <g fill="var(--mark)">
    <polygon points="5,36 22,8 39,36"/>
    <ellipse cx="100" cy="22" rx="19" ry="10" fill="none" stroke="var(--mark)" stroke-width="2"/>
    <rect x="161" y="4" width="36" height="36" rx="8"/>
    <circle cx="256" cy="21" r="19" fill="none" stroke="var(--mark)" stroke-width="2"/>
    <circle cx="335" cy="22" r="17"/>
    <circle cx="414" cy="22" r="17" fill="none" stroke="var(--mark)" stroke-width="2"/>
    <polygon points="470,30 500,14 510,18 480,34"/>
    <rect x="560" y="4" width="24" height="38" rx="10"/>
    <rect x="618" y="12" width="34" height="22"/>
    <polygon points="698,12 730,12 722,23 730,34 698,34"/>
    <circle cx="781" cy="23" r="15"/>
  </g>
</svg>
<div class="rule" style="top:788px"></div>

<footer class="site-footer">
  <span>© 2012 Drivlane. All Rights reserved. <a href="#">Terms &amp; Conditions</a></span>
  <span>Home &nbsp;-&nbsp; How it works &nbsp;-&nbsp; Prices &nbsp;-&nbsp; Our Customers &nbsp;-&nbsp; About us &nbsp;-&nbsp; Contact</span>
</footer>
</body>
</html>
```